Brennock transport business cards

Front of card, Looking for my logo on one side of the card

Back of card,
Brennock Transport Maintenance
Onsite Cars, Trucks & trailer maintenance and repairs
Gary Brennock
0452918406
Brennocktm@vexmail.test

```html
<!DOCTYPE html>
<html lang="en">
<head>
<meta charset="utf-8">
<title>Brennock transport business cards</title>
<link href="https://fonts.googleapis.com/css2?family=Bebas+Neue&family=Lato:wght@400&family=Michroma&display=swap" rel="stylesheet">
<style>
  :root {
    --backdrop: #2e2e2e;
    --card: #ffffff;
    --ink: #111111;
    --blue: #1e7fd8;
    --rule: #222222;
  }
  * { box-sizing: border-box; margin: 0; padding: 0; }
  html, body { width: 1200px; height: 694px; overflow: hidden; background: var(--backdrop); }
  .canvas {
    position: relative; width: 1200px; height: 694px;
    display: flex; align-items: center; justify-content: center; gap: 40px;
  }
  .card {
    position: relative; width: 540px; height: 300px;
    background: var(--card); border-radius: 22px; overflow: hidden;
  }

  /* Front */
  .front .brand {
    position: absolute; left: 60px; top: 52px;
    display: flex; align-items: center; gap: 16px;
  }
  .brand-square { width: 48px; height: 48px; background: var(--blue); }
  .front .brand-name {
    font-family: "Bebas Neue", sans-serif; font-size: 92px; line-height: 1;
    color: var(--ink); letter-spacing: 2px;
  }
  .front .brand-rule {
    position: absolute; left: 60px; right: 60px; top: 150px;
    height: 4px; background: var(--blue);
  }
  .front .phone-big {
    position: absolute; left: 0; right: 0; top: 178px; text-align: center;
    font-family: "Michroma", sans-serif; font-size: 44px; color: var(--ink);
    letter-spacing: 1px;
  }

  /* Back */
  .back .brand-mini {
    position: absolute; right: 40px; top: 30px; text-align: right;
  }
  .back .brand-mini .row { display: flex; align-items: center; justify-content: flex-end; gap: 8px; }
  .back .brand-mini .brand-square { width: 20px; height: 20px; }
  .back .brand-mini .brand-name {
    font-family: "Bebas Neue", sans-serif; font-size: 40px; line-height: 1; color: var(--ink);
  }
  .back .brand-mini .phone-small {
    font-family: "Michroma", sans-serif; font-size: 18px; color: var(--ink); margin-top: 4px;
  }
  .back .top-rule {
    position: absolute; left: 200px; right: 40px; top: 112px; height: 1px; background: var(--rule);
  }
  .back .services {
    position: absolute; right: 40px; top: 126px; text-align: right;
    font-family: "Lato", sans-serif; font-size: 15px; line-height: 1.45; color: var(--ink);
  }
  .back .bottom-rule {
    position: absolute; left: 30px; width: 330px; top: 196px; height: 1px; background: var(--rule);
  }
  .back .contact { position: absolute; left: 30px; top: 204px; }
  .back .person {
    font-family: "Bebas Neue", sans-serif; font-size: 30px; line-height: 1; color: var(--blue);
    margin-bottom: 6px;
  }
  .back .contact-line {
    display: flex; align-items: center; gap: 10px;
    font-family: "Lato", sans-serif; font-size: 15px; color: var(--ink); line-height: 1.55;
  }
  .back .contact-line svg { width: 16px; height: 16px; fill: var(--blue); flex: none; }
</style>
</head>
<body>
<main class="canvas">

  <section class="card front" aria-label="Card front">
    <div class="brand">
      <span class="brand-square"></span>
      <span class="brand-name">Brennock</span>
    </div>
    <div class="brand-rule"></div>
    <div class="phone-big">0452918406</div>
  </section>

  <section class="card back" aria-label="Card back">
    <div class="brand-mini">
      <div class="row">
        <span class="brand-square"></span>
        <span class="brand-name">Brennock</span>
      </div>
      <div class="phone-small">0452918406</div>
    </div>
    <div class="top-rule"></div>
    <p class="services">
      • Brennock Transport Maintenance<br>
      • Onsite Cars • Trucks &amp; trailer<br>
      maintenance and repairs
    </p>
    <div class="bottom-rule"></div>
    <div class="contact">
      <div class="person">Gary Brennock</div>
      <div class="contact-line">
        <svg viewBox="0 0 24 24" aria-hidden="true"><path d="M6.6 10.8a15.1 15.1 0 0 0 6.6 6.6l2.2-2.2a1 1 0 0 1 1-.25 11.4 11.4 0 0 0 3.6.57 1 1 0 0 1 1 1V20a1 1 0 0 1-1 1A17 17 0 0 1 3 4a1 1 0 0 1 1-1h3.5a1 1 0 0 1 1 1c0 1.25.2 2.45.57 3.57a1 1 0 0 1-.25 1z"/></svg>
        <span>0452918406</span>
      </div>
      <div class="contact-line">
        <svg viewBox="0 0 24 24" aria-hidden="true"><path d="M2 5h20v14H2zm2 2v.5l8 5 8-5V7l-8 5z"/></svg>
        <span>Brennocktm@vexmail.test</span>
      </div>
    </div>
  </section>

</main>
</body>
</html>
```